Eye catching and professional flyer

We would like a flyer done for promo, predominately attached to emails and printed to advertise our business. We provide employment advice to Employers so its pretty straight forward. Shouldn't need lots of words. Needs to be catchy, exude confidence and look slick and professional.

Attached is our logo, some general info you may choose to use and some headlines. These are real headlines that we thought might be cool to be presented somehow as a hook and a fear motivator.
Updates

Project Deadline Extended Reason: I need the headlines to be displayed as though in newspaper. EG $5 squabble etc . Added Thursday, June 15, 2017

Target Market(s)

Employers in SME Companies

Industry/Entity Type

Business

Font styles to use
Serif
Sans Serif

Colors

Designer to choose colors to be used in the design.

Requirements
Must have
• Eye catching, professional. Imagery and pop out wording. Not lots and lots of text.
Should not have
• Be boring and amateur.

```html
<!DOCTYPE html>
<html lang="en">
<head>
<meta charset="utf-8">
<title>StaffSense – Employment Advice Flyer</title>
<link href="https://fonts.googleapis.com/css2?family=Lato:wght@400;700;900&display=swap" rel="stylesheet">
<style>
  :root{
    --orange:#f26a21;
    --orange-deep:#ef5a24;
    --charcoal:#3a393b;
    --ink:#333333;
    --white:#ffffff;
    --gold-light:#ecc885;
    --gold:#d4a04f;
    --gold-dark:#b7822f;
  }
  *{margin:0;padding:0;box-sizing:border-box}
  html,body{width:858px;height:1200px;overflow:hidden;background:var(--white)}
  body{font-family:"Lato",Arial,sans-serif;color:var(--ink)}
  .flyer{position:relative;width:858px;height:1200px;overflow:hidden;background:var(--white)}

  .dark-panel{position:absolute;left:11px;top:520px;width:837px;height:542px;background:var(--charcoal)}
  .hero-photo{position:absolute;left:0;top:0}
  .corner-band{position:absolute;left:0;top:0}

  .trial-tag{position:absolute;left:26px;top:84px;color:var(--orange-deep);font-weight:900;
    font-size:31px;line-height:34px;transform:rotate(-9deg);transform-origin:left top;text-align:center}

  .brand{position:absolute;right:24px;top:20px;text-align:right}
  .brand-name{font-weight:700;font-size:76px;line-height:84px;color:#2f2f31;letter-spacing:-1px}
  .brand-tagline{font-size:18px;color:var(--ink);margin-top:6px}

  .headline{position:absolute;left:18px;top:388px;color:var(--white);line-height:1}
  .headline .line{display:block;white-space:nowrap}
  .headline .big{font-weight:900;font-size:72px}
  .headline .small{font-weight:400;font-size:35px;margin:0 8px 0 12px}
  .headline .line2{margin-top:-6px}
  .headline .huge{display:block;font-weight:900;font-size:90px;margin-top:-8px}

  .clipping{position:absolute;left:416px;top:524px}
  .clipping-text{position:absolute;left:440px;top:628px;width:370px;transform:rotate(-10deg);
    color:#1f1f1f;text-align:center;font-size:38px;line-height:46px}
  .clipping-text b{font-weight:900;font-size:48px}

  .intro{position:absolute;left:36px;top:666px;width:360px;color:var(--white);font-size:20.5px;line-height:26px}
  .intro span{display:block;text-align:justify;text-align-last:justify}
  .intro .r{text-align:right;text-align-last:right}
  .intro .l{text-align:left;text-align-last:left}

  .services{position:absolute;list-style:none;color:var(--white);font-size:20.5px;line-height:21px}
  .services li{position:relative;padding-left:18px;margin-bottom:7.6px}
  .services li::before{content:"";position:absolute;left:1px;top:6px;width:9px;height:9px;border-radius:50%;background:var(--orange)}
  .services-left{left:20px;top:814px;width:412px}
  .services-right{left:448px;top:814px;width:380px}

  .closing{position:absolute;left:0;top:1068px;width:858px;text-align:center;font-size:17.5px;line-height:23px;color:var(--ink)}
  .closing p+p{margin-top:6px}

  .contact-bar{position:absolute;left:0;top:1148px;width:858px;height:52px;background:var(--orange);
    color:var(--white);display:flex;justify-content:center;align-items:center;gap:16px;font-size:23px}
  .contact-bar .sep{font-weight:900}
</style>
</head>
<body>
<div class="flyer">
  <div class="dark-panel"></div>

  <svg class="hero-photo" width="858" height="680" viewBox="0 0 858 680" role="img" aria-label="Photo of smiling business people in dark suits and white shirts shaking hands around a meeting table">
    <defs>
      <linearGradient id="heroTone" x1="0" y1="0" x2="0" y2="1">
        <stop offset="0" stop-color="#ffffff"/>
        <stop offset="0.12" stop-color="#eeeeee"/>
        <stop offset="0.24" stop-color="#c4c4c6"/>
        <stop offset="0.38" stop-color="#7a7a7d"/>
        <stop offset="0.52" stop-color="#3e3e41"/>
        <stop offset="0.75" stop-color="#222224"/>
        <stop offset="1" stop-color="#1a1a1c"/>
      </linearGradient>
      <radialGradient id="shirtGlow" cx="0.5" cy="0.5" r="0.5">
        <stop offset="0" stop-color="#e6e8ee" stop-opacity="0.55"/>
        <stop offset="1" stop-color="#e6e8ee" stop-opacity="0"/>
      </radialGradient>
      <radialGradient id="suitShade" cx="0.5" cy="0.5" r="0.5">
        <stop offset="0" stop-color="#0f0f11" stop-opacity="0.6"/>
        <stop offset="1" stop-color="#0f0f11" stop-opacity="0"/>
      </radialGradient>
    </defs>
    <polygon points="0,0 858,0 858,531 0,675" fill="url(#heroTone)"/>
    <ellipse cx="120" cy="320" rx="160" ry="150" fill="url(#suitShade)"/>
    <ellipse cx="760" cy="330" rx="150" ry="170" fill="url(#suitShade)"/>
    <ellipse cx="370" cy="300" rx="70" ry="110" fill="url(#shirtGlow)"/>
    <ellipse cx="560" cy="320" rx="70" ry="110" fill="url(#shirtGlow)"/>
  </svg>

  <svg class="corner-band" width="460" height="70" viewBox="0 0 460 70" aria-hidden="true">
    <polygon points="0,0 445,0 0,66" fill="var(--orange)"/>
  </svg>
  <div class="trial-tag">No contract rules<br>out 90 day trial</div>

  <div class="brand">
    <div class="brand-name">staffsense</div>
    <div class="brand-tagline">Intelligent Employment Advice</div>
  </div>

  <div class="headline">
    <span class="line"><span class="big">Employee</span><span class="small">tells boss to stick job, then</span></span>
    <span class="line line2"><span class="big">wins</span><span class="small">pay out for</span><span class="big">constructive</span></span>
    <span class="huge">dismissal</span>
  </div>

  <svg class="clipping" width="420" height="290" viewBox="0 0 420 290" aria-hidden="true">
    <defs>
      <radialGradient id="paperTone" cx="0.45" cy="0.45" r="0.7">
        <stop offset="0" stop-color="var(--gold-light)"/>
        <stop offset="0.6" stop-color="var(--gold)"/>
        <stop offset="1" stop-color="var(--gold-dark)"/>
      </radialGradient>
    </defs>
    <polygon points="20,104 60,92 96,80 140,72 182,58 222,52 262,48 300,34 338,28 372,16 398,22 404,62 396,100 404,136 398,176 404,208 390,242 352,248 312,254 272,260 230,266 190,272 150,274 110,280 72,278 40,272 22,246 30,206 18,176 26,146 16,124"
      fill="url(#paperTone)" stroke="var(--white)" stroke-width="7" stroke-linejoin="round"/>
  </svg>
  <div class="clipping-text"><b>$5</b> squabble turns<br>to <b>$12k</b> payout</div>

  <div class="intro">
    <span class="r">We offer direct</span>
    <span class="r">and helpful advice. We are cost</span>
    <span>effective and understand the needs of</span>
    <span>business. We are about solving</span>
    <span class="l">problems, not protracting them.</span>
  </div>

  <ul class="services services-left">
    <li>Personal grievances raised against you by<br>an Employee</li>
    <li>Independent Employment Investigations</li>
    <li>Investigation Meetings</li>
    <li>Disciplinary Meetings</li>
    <li>Misconduct and Serious Misconduct</li>
    <li>Employee dismissals</li>
    <li>Abuse of sick leave</li>
  </ul>
  <ul class="services services-right">
    <li>Restructuring and Redundancies</li>
    <li>Employment contracts drafting and checking</li>
    <li>Poor performers</li>
    <li>90 day trials</li>
    <li>Workplace drug testing advice</li>
    <li>Parental leave</li>
    <li>Exit management</li>
    <li>Medical Incapacity</li>
  </ul>

  <div class="closing">
    <p>Introducing StaffSense the smart choice for Employers needing Intelligent Employment Advice.</p>
    <p>We will with any Employment problem from checking that your employment contracts are current<br>through to dealing with disputes and grieavances.</p>
  </div>

  <div class="contact-bar">
    <span>0800 55 44 11</span><span class="sep">|</span>
    <span>help@staffsense.co.nz</span><span class="sep">|</span>
    <span>www.staffsense.co.nz</span>
  </div>
</div>
</body>
</html>
```